Young Accounting firm needing a captivating business card

We need a business card design that forces the person to look at the card because its either gold foil, plastic, or lettering pop up etc. We already have a logo with a specific gold color and we need to make it pop. We are an accounting firm. I need the words" accounting, payroll, licenses, audits, taxes" somewhere on the business card so as to describe what we do- preferably on the side where the logo is at.

Industry/Entity Type

Accounting

Contact Information for Business Card

Address 48276 9th Ave S Ste 305, Maple Ridge, OR 97117
Business Phone (541)418-2096
Fax (541)418-2157
Office Cell Phone (541)586-7319

Font styles to use
Serif

Colors
85abd2

Requirements
Must have
• It should state
• "Accounting" "Taxes" "Audits" "Licenses" "Payroll"
Nice to have
• Matte with gold foil, different textures, With Either a textured ivory background or gray blue slate background
Should not have
• colorful colors

```html
<!DOCTYPE html>
<html lang="en">
<head>
<meta charset="utf-8">
<title>Kelmont Ledger – Business Card</title>
<link href="https://fonts.googleapis.com/css2?family=Work+Sans:wght@400;500&display=swap" rel="stylesheet">
<style>
  :root {
    --backdrop: #232323;
    --paper: #f1f1f1;
    --slate: #353535;
    --slate-band: #3d3d3d;
    --gold: #bb9816;
    --ink: #4a4a4a;
    --white: #f4f4f4;
  }
  * { box-sizing: border-box; margin: 0; padding: 0; }
  html, body { width: 1200px; height: 900px; overflow: hidden; }
  body {
    background: var(--backdrop);
    font-family: "Work Sans", sans-serif;
    position: relative;
  }
  .card {
    position: absolute;
    left: 261px;
    width: 656px;
    height: 357px;
    box-shadow: 0 4px 14px rgba(0,0,0,.45);
    overflow: hidden;
  }
  .card-front { top: 69px; background: var(--paper); }
  .card-back { top: 472px; background: var(--slate); }

  .front-swoop { position: absolute; left: 0; top: 0; width: 656px; height: 357px; }

  .brand-name {
    position: absolute;
    color: var(--gold);
    font-weight: 500;
    white-space: nowrap;
    display: flex;
    align-items: center;
    gap: 12px;
  }
  .brand-mark {
    width: 14px; height: 14px;
    background: var(--gold);
    display: inline-block;
  }
  .card-front .brand-name {
    left: 0; width: 350px; top: 196px;
    justify-content: center;
    font-size: 34px;
    line-height: 40px;
    letter-spacing: -0.5px;
  }
  .divider {
    position: absolute;
    left: 350px; top: 81px;
    width: 2px; height: 196px;
    background: var(--gold);
  }
  .contact {
    position: absolute;
    left: 389px; top: 74px;
    color: var(--ink);
  }
  .contact-name {
    color: var(--gold);
    font-weight: 500;
    font-size: 30px;
    line-height: 36px;
  }
  .contact-title { font-size: 16px; line-height: 18px; margin-bottom: 10px; }
  .contact-address { font-size: 15.5px; line-height: 20px; margin-bottom: 8px; letter-spacing: .3px; }
  .contact-list { list-style: none; }
  .contact-list li {
    display: flex; align-items: center; gap: 8px;
    font-size: 15.5px; line-height: 20px; letter-spacing: .3px;
  }
  .contact-list svg { width: 10px; height: 10px; flex: none; }

  .card-back .brand-name {
    left: 0; width: 656px; top: 200px;
    justify-content: center;
    font-size: 40px;
    line-height: 46px;
    letter-spacing: -0.5px;
  }
  .services {
    position: absolute;
    left: 0; width: 656px; top: 319px;
    text-align: center;
    color: var(--white);
    font-size: 17px;
    line-height: 22px;
    letter-spacing: .4px;
  }
  .services .sep { color: var(--gold); margin: 0 5px; }
  .services .sep-plain { margin: 0 5px; }
</style>
</head>
<body>

<section class="card card-front">
  <svg class="front-swoop" viewBox="0 0 656 357" aria-hidden="true">
    <path d="M0 285 C 150 340, 420 365, 656 315 L656 357 L0 357 Z" fill="var(--slate-band)"/>
    <path d="M105 309 C 260 345, 470 345, 656 298 L656 308 C 470 350, 260 348, 105 309 Z" fill="var(--gold)"/>
  </svg>

  <div class="brand-name"><span class="brand-mark"></span>Kelmont Ledger</div>
  <div class="divider"></div>

  <div class="contact">
    <div class="contact-name">Darren Holloway</div>
    <div class="contact-title">Director</div>
    <div class="contact-address">48276 9th Ave S Ste 305,<br>Maple Ridge, OR 97117</div>
    <ul class="contact-list">
      <li>
        <svg viewBox="0 0 10 10"><path d="M2 0.5 L3.6 2.8 L2.7 3.8 C3.3 5.3 4.6 6.6 6.1 7.2 L7.1 6.3 L9.5 8 L8.2 9.6 C4.4 9.3 0.7 5.6 0.4 1.8 Z" fill="var(--gold)"/></svg>
        (541)418-2096
      </li>
      <li>
        <svg viewBox="0 0 10 10"><rect x="2.5" y="0.5" width="5" height="2.5" fill="var(--gold)"/><rect x="0.5" y="3.5" width="9" height="4" rx="1" fill="var(--gold)"/><rect x="2.5" y="7" width="5" height="2.5" fill="var(--gold)"/></svg>
        (541)418-2157
      </li>
      <li>
        <svg viewBox="0 0 10 10"><rect x="2.5" y="0.5" width="5" height="9" rx="1" fill="none" stroke="var(--gold)" stroke-width="1.2"/><circle cx="5" cy="7.8" r=".6" fill="var(--gold)"/></svg>
        (541)586-7319
      </li>
      <li>
        <svg viewBox="0 0 10 10"><rect x="0.6" y="2" width="8.8" height="6" fill="none" stroke="var(--gold)" stroke-width="1.1"/><path d="M0.8 2.3 L5 5.5 L9.2 2.3" fill="none" stroke="var(--gold)" stroke-width="1.1"/></svg>
        info@kelmontledger.com
      </li>
      <li>
        <svg viewBox="0 0 10 10"><circle cx="5" cy="5" r="4.3" fill="none" stroke="var(--gold)" stroke-width="1"/><ellipse cx="5" cy="5" rx="1.8" ry="4.3" fill="none" stroke="var(--gold)" stroke-width=".8"/><path d="M0.8 5 H9.2 M1.5 2.8 H8.5 M1.5 7.2 H8.5" stroke="var(--gold)" stroke-width=".8"/></svg>
        www.kelmontledger.com
      </li>
    </ul>
  </div>
</section>

<section class="card card-back">
  <div class="brand-name"><span class="brand-mark"></span>Kelmont Ledger</div>
  <p class="services">
    Accounting<span class="sep">|</span>Payroll<span class="sep">|</span>Licenses<span class="sep">|</span>Audits<span class="sep-plain">|</span>Taxes
  </p>
</section>

</body>
</html>
```